Aerial Imaging and photgraphy business card

Design a business card with eye catching aerial photo of country side / landscape with a drone in the foreground.
Also contact details.

Target Market(s)

Aerial Imaging photography

Industry/Entity Type

Advertising

Contact Information for Business Card

Corwin
0412905316
Website http://www.skylarkvistas.com.au/
email address : skylarkvistas.com.au

Colors
e8f1ca
cadf82
9bcb3c
33a6d7
85cae6
cee9f5

Requirements
Must have
• High res photo
• KPV drone in the foreground Either T4200 and kpv Hovera or both
Nice to have
• high resolution landscape country photo on the front of the card with a KPV T4200 drone in the foreground.

```html
<!DOCTYPE html>
<html lang="en">
<head>
<meta charset="utf-8">
<title>Skylark Vistas – Business Card</title>
<link href="https://fonts.googleapis.com/css2?family=Open+Sans:wght@300;400;600;700&display=swap" rel="stylesheet">
<style>
  :root {
    --page-bg: #e9e6df;
    --card-white: #ffffff;
    --ink-grey: #4a4a4a;
    --ink-soft: #6b6b6b;
    --accent-red: #d8262e;
    --accent-green: #7cbf3a;
    --sky-light: #cee9f5;
    --sky-mid: #a9c7d6;
    --haze: #dfe3e4;
    --field-green: #6f8f45;
    --field-dark: #4e6a30;
  }
  * { box-sizing: border-box; margin: 0; padding: 0; }
  html, body { width: 771px; height: 1200px; overflow: hidden; }
  body {
    background: var(--page-bg);
    font-family: "Open Sans", Arial, sans-serif;
    position: relative;
  }
  .card {
    position: absolute;
    left: 65px;
    width: 640px;
    height: 366px;
    border-radius: 16px;
    overflow: hidden;
    background: var(--card-white);
    box-shadow: 0 6px 18px rgba(0,0,0,0.18);
  }
  .card--front { top: 140px; }
  .card--back { top: 694px; }

  .card__art { position: absolute; inset: 0; width: 100%; height: 100%; }

  .brand {
    position: absolute;
    display: flex;
    align-items: center;
    gap: 10px;
    color: var(--ink-grey);
    font-weight: 700;
    letter-spacing: 0.04em;
    text-transform: uppercase;
  }
  .brand__dot {
    border-radius: 50%;
    background: var(--ink-grey);
    flex: none;
  }
  .card--front .brand { left: 36px; top: 70px; font-size: 22px; }
  .card--front .brand__dot { width: 26px; height: 26px; }

  .person { position: absolute; left: 150px; top: 178px; }
  .person__name {
    font-weight: 300;
    font-size: 36px;
    color: var(--ink-grey);
    line-height: 1.1;
  }
  .person__title {
    font-size: 13px;
    color: var(--accent-red);
    letter-spacing: 0.06em;
    margin-top: 4px;
  }

  .contacts {
    position: absolute;
    left: 150px;
    top: 262px;
    list-style: none;
    font-size: 13px;
    color: var(--ink-grey);
  }
  .contacts__row { display: flex; align-items: center; gap: 8px; margin-bottom: 8px; }
  .contacts__icon { width: 13px; height: 13px; flex: none; }
  .contacts__pair { display: flex; gap: 28px; }

  .card--back .brand {
    left: 0; right: 0; top: 160px;
    justify-content: center;
    font-size: 34px;
  }
  .card--back .brand__dot { width: 36px; height: 36px; }
</style>
</head>
<body>

  <section class="card card--front" aria-label="Business card front">
    <svg class="card__art" viewBox="0 0 640 366" aria-hidden="false">
      <defs>
        <linearGradient id="landscape" x1="0" y1="0" x2="0" y2="1">
          <stop offset="0" stop-color="#cee9f5"/>
          <stop offset="0.35" stop-color="#b9cdd6"/>
          <stop offset="0.55" stop-color="#7f9a5a"/>
          <stop offset="1" stop-color="#4e6a30"/>
        </linearGradient>
      </defs>
      <path role="img" aria-label="Aerial photo of green rolling countryside with a drone hovering in the foreground"
            d="M250 0 H640 V366 H585 Q440 140 250 0 Z" fill="url(#landscape)"/>
      <path class="card__curve" d="M250 0 Q440 140 585 366" fill="none" stroke="var(--accent-red)" stroke-width="4"/>
    </svg>

    <div class="brand"><span class="brand__dot"></span>Skylark Vistas</div>

    <div class="person">
      <p class="person__name">Your Name</p>
      <p class="person__title">JOB TITLE</p>
    </div>

    <ul class="contacts">
      <li class="contacts__pair">
        <span class="contacts__row">
          <svg class="contacts__icon" viewBox="0 0 16 16"><rect width="16" height="16" rx="3" fill="var(--accent-green)"/><path d="M5 4c1 0 1.5 2 1 2.5S6 8 8 10s2.5 1.5 3 1 2.5 0 2.5 1-1.5 1.5-2.5 1.5C7 13.5 2.5 9 2.5 5.5 2.5 4.5 4 4 5 4z" fill="#fff"/></svg>
          000 000 0000
        </span>
        <span class="contacts__row">
          <svg class="contacts__icon" viewBox="0 0 16 16"><rect width="16" height="16" rx="3" fill="var(--accent-green)"/><path d="M3 5h10v6H3z M3 5l5 4 5-4" fill="none" stroke="#fff" stroke-width="1.3"/></svg>
          email@skyvis.com
        </span>
      </li>
      <li class="contacts__row">
        <svg class="contacts__icon" viewBox="0 0 16 16"><circle cx="8" cy="8" r="8" fill="var(--accent-green)"/><circle cx="8" cy="8" r="4.5" fill="none" stroke="#fff" stroke-width="1.2"/><path d="M3.5 8h9M8 3.5v9" stroke="#fff" stroke-width="1.2"/></svg>
        www.skylarkvistas.com.au
      </li>
    </ul>
  </section>

  <section class="card card--back" aria-label="Business card back">
    <svg class="card__art" viewBox="0 0 640 366">
      <defs>
        <linearGradient id="hazySky" x1="0" y1="0" x2="0" y2="1">
          <stop offset="0" stop-color="#a9c7d6"/>
          <stop offset="0.5" stop-color="#dfe3e4"/>
          <stop offset="1" stop-color="#c9cfd1"/>
        </linearGradient>
      </defs>
      <rect role="img" aria-label="Hazy aerial photo of a wide landscape with a drone flying on the left"
            width="640" height="366" fill="url(#hazySky)"/>
    </svg>
    <div class="brand"><span class="brand__dot"></span>Skylark Vistas</div>
  </section>

</body>
</html>
```